CD Cover Design Project

I need a cd cover design for my first 5-song EP which is going to be released on March 1st. I am a 19 year old female singer/songwriter based in Nashville, TN, and my style is somewhat singer/songwriter and/or pop/rock (ex: Delphine Waverly, Maren Tolk...if you don't know these references, please check them out). I believe that simplicity is key, and this cover design should not be too overboard but should still express creativity with a touch of boldness, if that makes sense.
Updates
Can you all try putting the image with my hand in my hair (the mountains in the background) as the front cover and the bridge picture on the back cover?
I uploaded a picture of a font that i really like :) please check it out!
Hey everyone :) Thank you so much for submitting your awesome designs! We're all still swapping feedback and I'm still checking out what you all have created. I am uploading some examples of covers I really like, just so you can get the idea of what I like and dislike :) Thanks! Happy creating!
I AM UPLOADING A COLOR VERSION OF THE PICTURE I REALLY WANT TO USE AS THE FRONT COVER..... :)
Industry/Entity Type
Singer
Look and feel
Each slider illustrates characteristics of the customer's brand and the style your logo design should communicate.

```html
<!DOCTYPE html>
<html lang="en">
<head>
<meta charset="UTF-8">
<title>Sawyer Hollis – Slow the hours</title>
<link href="https://fonts.googleapis.com/css2?family=Bebas+Neue&family=Dancing+Script:wght@600&display=swap" rel="stylesheet">
<style>
  :root {
    --sky: #c4c690;
    --sky-warm: #d3c88e;
    --treeline: #86784f;
    --water: #7d8570;
    --water-deep: #6f7a66;
    --dock: #c9a468;
    --dock-shade: #8a7a5a;
    --glow-orange: rgba(235, 120, 60, 0.55);
    --glow-red: rgba(200, 60, 70, 0.45);
    --frame: rgba(255, 255, 255, 0.32);
    --ink-white: #f8f6ee;
    --ink-yellow: #f2c230;
    --ink-pink: #c43a5e;
  }
  * { margin: 0; padding: 0; box-sizing: border-box; }
  html, body { width: 1200px; height: 1025px; overflow: hidden; background: #ffffff; }
  .cover-back {
    position: relative;
    width: 1200px;
    height: 1025px;
    overflow: hidden;
    font-family: "Bebas Neue", "Oswald", sans-serif;
  }
  .lake-photo {
    position: absolute;
    inset: 0;
    background:
      radial-gradient(ellipse 380px 520px at 1200px 330px, var(--glow-orange), transparent 75%),
      radial-gradient(ellipse 420px 300px at 80px 900px, var(--glow-red), transparent 75%),
      linear-gradient(180deg,
        var(--sky) 0%,
        var(--sky-warm) 28%,
        var(--treeline) 34%,
        var(--treeline) 42%,
        var(--water) 46%,
        var(--water-deep) 62%,
        var(--dock) 68%,
        var(--dock) 80%,
        var(--dock-shade) 88%,
        var(--water-deep) 100%);
  }
  .frame {
    position: absolute;
    left: 22px;
    top: 22px;
    width: 1075px;
    height: 978px;
    border: 33px solid var(--frame);
  }
  .artist-name {
    position: absolute;
    left: 0;
    width: 1104px;
    top: 102px;
    text-align: center;
    font-size: 114px;
    font-weight: 400;
    line-height: 1;
    letter-spacing: 3px;
    color: var(--ink-white);
  }
  .release-title {
    position: absolute;
    left: 0;
    width: 1104px;
    top: 182px;
    text-align: center;
    font-family: "Dancing Script", cursive;
    font-weight: 600;
    font-size: 52px;
    line-height: 1.2;
    color: var(--ink-yellow);
  }
  .tracklist {
    position: absolute;
    left: 0;
    width: 1120px;
    top: 468px;
    list-style: none;
    text-align: center;
    font-size: 50px;
    line-height: 63px;
    letter-spacing: 1.5px;
    color: var(--ink-white);
  }
  .tracklist li { display: inline; margin: 0 10px; }
  .tracklist .track-no { color: var(--ink-yellow); }
  .tracklist .line-break { display: block; height: 0; }
  .spine-title {
    position: absolute;
    left: 1118px;
    top: 98px;
    writing-mode: vertical-rl;
    font-family: "Dancing Script", cursive;
    font-weight: 600;
    font-size: 42px;
    line-height: 1;
    color: var(--ink-pink);
  }
  .spine-artist {
    position: absolute;
    left: 1115px;
    top: 688px;
    writing-mode: vertical-rl;
    font-size: 46px;
    line-height: 1;
    letter-spacing: 2px;
    color: var(--ink-white);
  }
</style>
</head>
<body>
  <main class="cover-back">
    <div class="lake-photo" role="img" aria-label="Photograph of a weathered wooden dock on a calm lake with a bare tree line under a hazy sky, in faded warm tones"></div>
    <div class="frame"></div>

    <h1 class="artist-name">Sawyer Hollis</h1>
    <p class="release-title">Slow the hours</p>

    <ol class="tracklist">
      <li><span class="track-no">1.</span>Dusty</li>
      <li><span class="track-no">2.</span>Slow the Hours</li>
      <li><span class="track-no">3.</span>Hold On and Stay</li>
      <span class="line-break"></span>
      <li><span class="track-no">4.</span>Ten Long Miles</li>
      <li><span class="track-no">5.</span>Only for Me</li>
    </ol>

    <p class="spine-title">Slow the hours</p>
    <p class="spine-artist">Sawyer Hollis</p>
  </main>
</body>
</html>
```